Business Card

We would like a very clean corporate, two sided business card that conveys that we are a quality focused, reliable organisation that can make a business better. We focus on a cycle of continuous improvement for IT systems.

The brief is primarily clean and corporate, nothing overly complicated.

We sell IT services, IT support, server implementation, problem solving services to businesses in Australia.

Business

```html
<!DOCTYPE html>
<html lang="en">
<head>
<meta charset="utf-8">
<title>tarnevio business card</title>
<link rel="stylesheet" href="https://fonts.googleapis.com/css2?family=Ubuntu:wght@500&family=Arimo:wght@400;500&family=Cinzel:wght@400&display=swap">
<style>
  :root {
    --backdrop: #d6d6d7;
    --card-edge: #e8e8e9;
    --panel-light: #ffffff;
    --panel-shade: #dadadb;
    --brand-red: #b5000c;
    --brand-red-dark: #8e0009;
    --ink: #161616;
    --rule: #555555;
    --label: #3a3a3a;
  }
  html, body {
    margin: 0;
    padding: 0;
    overflow: hidden;
  }
  body {
    width: 1200px;
    height: 895px;
    background: var(--backdrop);
    position: relative;
    font-family: "Arimo", Arial, sans-serif;
  }
  .card {
    position: absolute;
    top: 302px;
    width: 568px;
    height: 342px;
    border-radius: 14px;
    background: var(--card-edge);
  }
  .card--front { left: 18px; }
  .card--back { left: 612px; }
  .card__panel {
    position: absolute;
    left: 21px;
    top: 16px;
    right: 18px;
    bottom: 18px;
    border-radius: 22px;
    background: radial-gradient(ellipse at 45% 20%, var(--panel-light) 0%, #f1f1f2 45%, var(--panel-shade) 100%);
  }
  .band {
    position: absolute;
    top: 169px;
    height: 36px;
    background: linear-gradient(to bottom,
      var(--brand-red) 0, var(--brand-red-dark) 12px,
      #f4f4f4 12px, #c9c9c9 22px,
      var(--brand-red) 22px, var(--brand-red-dark) 36px);
  }
  .card--front .band--left { left: 21px; width: 127px; }
  .card--front .band--right { left: 422px; width: 128px; }
  .card--back .band--right { left: 323px; width: 227px; }
  .wordmark {
    position: absolute;
    display: flex;
    align-items: center;
    gap: 10px;
    font-family: "Ubuntu", sans-serif;
    font-weight: 500;
    color: var(--ink);
    white-space: nowrap;
  }
  .wordmark__dot {
    background: var(--brand-red);
    flex: none;
  }
  .card--front .wordmark {
    left: 172px;
    top: 118px;
    font-size: 44px;
  }
  .card--front .wordmark__dot { width: 18px; height: 18px; }
  .card--back .wordmark {
    left: 323px;
    top: 122px;
    font-size: 26px;
    gap: 7px;
  }
  .card--back .wordmark__dot { width: 11px; height: 11px; }
  .contact {
    position: absolute;
    right: 304px;
    top: 116px;
    text-align: right;
    color: var(--ink);
  }
  .contact__name {
    margin: 0 0 12px;
    font-size: 17px;
    font-weight: 500;
    color: var(--brand-red);
  }
  .contact__line {
    margin: 0;
    font-size: 12px;
    line-height: 14px;
    letter-spacing: 0.3px;
  }
  .contact__phones { margin-top: 4px; }
  .contact__phone {
    margin: 0;
    font-size: 14px;
    line-height: 14px;
    letter-spacing: 1.4px;
  }
  .contact__rule {
    position: absolute;
    left: 275px;
    top: 100px;
    width: 1px;
    height: 142px;
    background: var(--rule);
  }
  .contact__icons {
    position: absolute;
    left: 287px;
    top: 158px;
    display: flex;
    flex-direction: column;
    gap: 3px;
  }
  .contact__icons svg { display: block; }
  .view-label {
    position: absolute;
    top: 686px;
    font-family: "Cinzel", serif;
    font-size: 14px;
    letter-spacing: 3px;
    color: var(--label);
  }
  .view-label--front { left: 66px; }
  .view-label--back { left: 659px; }
</style>
</head>
<body>
  <section class="card card--front" aria-label="Card front">
    <div class="card__panel"></div>
    <div class="band band--left"></div>
    <div class="band band--right"></div>
    <div class="wordmark">tarnevio<span class="wordmark__dot"></span></div>
  </section>

  <section class="card card--back" aria-label="Card back">
    <div class="card__panel"></div>
    <div class="contact">
      <p class="contact__name">Sam Carter</p>
      <p class="contact__line">www.tarnevio.net</p>
      <p class="contact__line">sam.carter@tarnevio.net</p>
      <div class="contact__phones">
        <p class="contact__phone">123 456 7890</p>
        <p class="contact__phone">123 456 7890</p>
        <p class="contact__phone">123 456 7890</p>
      </div>
    </div>
    <div class="contact__rule"></div>
    <div class="contact__icons">
      <svg width="14" height="11" viewBox="0 0 14 11" aria-label="email"><rect x="0.5" y="0.5" width="13" height="10" fill="#b5000c"/><path d="M1 1 L7 6 L13 1" stroke="#fff" stroke-width="1.2" fill="none"/></svg>
      <svg width="14" height="11" viewBox="0 0 14 11" aria-label="fax"><rect x="3" y="0" width="8" height="4" fill="#b5000c"/><rect x="0" y="4" width="14" height="5" fill="#b5000c"/><rect x="3" y="7" width="8" height="4" fill="#fff" stroke="#b5000c"/></svg>
      <svg width="14" height="11" viewBox="0 0 14 11" aria-label="phone"><path d="M0 3 Q7 -1 14 3 L12 5 L10 4 L10 2.5 Q7 1.5 4 2.5 L4 4 L2 5 Z" fill="#b5000c"/><rect x="2" y="6" width="10" height="5" fill="#b5000c"/><circle cx="7" cy="8.5" r="1.3" fill="#fff"/></svg>
      <svg width="14" height="12" viewBox="0 0 14 12" aria-label="mobile"><rect x="1" y="0" width="12" height="12" rx="1" fill="#b5000c"/><rect x="3" y="2" width="8" height="3" fill="#fff"/><rect x="3" y="7" width="2" height="1.5" fill="#fff"/><rect x="6" y="7" width="2" height="1.5" fill="#fff"/><rect x="9" y="7" width="2" height="1.5" fill="#fff"/><rect x="3" y="9.5" width="2" height="1.5" fill="#fff"/><rect x="6" y="9.5" width="2" height="1.5" fill="#fff"/><rect x="9" y="9.5" width="2" height="1.5" fill="#fff"/></svg>
    </div>
    <div class="wordmark">tarnevio<span class="wordmark__dot"></span></div>
    <div class="band band--right"></div>
  </section>

  <div class="view-label view-label--front">FRONT</div>
  <div class="view-label view-label--back">BACK</div>
</body>
</html>
```